TLM Facebook Page Cover Image

I am setting up a Facebook company page for my new business called 'TimberLineMetrics'. We provide business owners, executives, and managers with valuable information via a comprehensive suite of employee assessment products to make better people decisions. Company tagline is Recruit Wisely - Grow Teams - Reach Goals. I need a attention grabbing, polished, professional cover graphic to be displayed on the top of the page that captures who we are and is a nice compliment to our logo which will appear in the smaller logo box. Company personality is contemporary, energetic, competent yet humble. Logo is attached. Please view our 3 minute overview video on YouTube to get a sense of who we are/what we do. https://www.videohostsample.com/watch?v=Qa7nRt2LmWz

Target Market(s)

My website is a B2B website. My ideal "sweet spot" client company employees approximately 200-300 employees, although my secondary products and service market will include companies above 200-300 employees to include select Meridian 400 companies. Target client roles within these companies include:
- Business Leaders - CEO's, Presidents, and General Managers
- Small & Mid-sized business owners
- Functional Leaders - CFOs, CIO, Sales/Marketing leaders, HR leaders
- Functional Specialists - Recruiting, Learning & Development, OD
- 1st and 2nd line managers
Our products and services can be used effectively across all industries, but if I had to pick the top 5 or 6 "target" industries or type of businesses that match extremely well to our products/services I'd say retail/consumer products, healthcare/human services, direct/outside sales (*e.g. car dealers, medical equipment sales, telemarketing, etc.), customer service call centers, hospitality, and banking.

Industry/Entity Type

Business

Font styles to use
Sans Serif

Requirements
Nice to have
• Don't want the graphic to be too busy or crowded. Photography and/or from scratch graphics can be used separately or in combination. Attached is a sample from an unrelated web page I like in terms of it's white space/graphic/text balance.

```html
<!DOCTYPE html>
<html lang="en">
<head>
<meta charset="utf-8">
<title>TimberLineMetrics Cover</title>
<link rel="stylesheet" href="https://fonts.googleapis.com/css2?family=Questrial&display=swap">
<style>
  :root {
    --page-bg: #eef1f5;
    --cover-top: #ffffff;
    --cover-mid: #eaf2f8;
    --map-light: #dbe8f1;
    --map-deep: #a9c4d8;
    --brand-blue: #1b7fc4;
    --ink: #2b2e34;
    --dot: #1f2a4d;
    --rule: #7b8794;
    --badge: #d9bf7a;
    --badge-edge: #b39549;
    --frame: #ffffff;
    --frame-edge: #c9ced6;
    --logo-bg: #e7eef5;
    --logo-ink: #1d3f7a;
  }
  * { margin: 0; padding: 0; box-sizing: border-box; }
  html, body {
    width: 1200px; height: 574px; overflow: hidden;
    background: var(--page-bg);
    font-family: "Questrial", "Century Gothic", sans-serif;
  }
  .canvas { position: relative; width: 1200px; height: 574px; }

  .cover {
    position: absolute; left: 25px; top: 60px;
    width: 1150px; height: 422px; overflow: hidden;
    background: linear-gradient(180deg, var(--cover-top) 0%, var(--cover-top) 45%, var(--cover-mid) 62%, var(--map-light) 100%);
    border: 1px solid var(--frame-edge);
  }
  .world-map {
    position: absolute; left: 0; right: 0; top: 250px; bottom: 0;
    background:
      radial-gradient(ellipse 60% 70% at 30% 70%, rgba(169,196,216,.55), transparent 70%),
      radial-gradient(ellipse 55% 60% at 72% 55%, rgba(169,196,216,.5), transparent 70%),
      linear-gradient(180deg, rgba(219,232,241,0) 0%, var(--map-light) 100%);
  }
  .connector { position: absolute; left: 0; top: 0; }

  .pillar { position: absolute; top: 48px; width: 300px; text-align: center; }
  .pillar svg { display: block; margin: 0 auto; }
  .pillar-label {
    display: block; margin-top: 22px;
    font-size: 35px; color: var(--brand-blue); letter-spacing: .3px; white-space: nowrap;
  }
  .pillar--recruit { left: 228px; }
  .pillar--grow { left: 578px; }
  .pillar--reach { left: 880px; }

  .separator {
    position: absolute; top: 179px; width: 14px; height: 14px;
    border-radius: 50%; background: var(--dot);
  }
  .separator--one { left: 520px; }
  .separator--two { left: 840px; }

  .partner-badge {
    position: absolute; left: 998px; top: 372px; width: 128px; height: 40px;
    background: linear-gradient(180deg, #e8d394, var(--badge));
    border: 1px solid var(--badge-edge);
  }

  .profile-frame {
    position: absolute; left: 54px; top: 343px; width: 228px; height: 228px;
    background: var(--frame); border: 1px solid var(--frame-edge); padding: 6px;
    box-shadow: 0 1px 3px rgba(0,0,0,.15);
  }
  .profile-logo {
    width: 100%; height: 100%;
    background: linear-gradient(160deg, #ffffff 0%, var(--logo-bg) 100%);
    display: flex; flex-direction: column; align-items: center; justify-content: center; gap: 14px;
  }
  .logo-mark { width: 58px; height: 58px; border-radius: 50%; background: var(--logo-ink); }
  .logo-name { font-size: 21px; color: var(--logo-ink); }
</style>
</head>
<body>
<div class="canvas">
  <section class="cover">
    <div class="world-map" role="img" aria-label="Soft world map illustration in pale blue tones across the lower cover"></div>

    <svg class="connector" width="1150" height="422" aria-hidden="true">
      <polyline points="290,181 134,181 134,284" fill="none" stroke="var(--rule)" stroke-width="1.5"/>
    </svg>

    <div class="pillar pillar--recruit">
      <svg width="90" height="90" viewBox="0 0 90 90" aria-hidden="true">
        <circle cx="38" cy="38" r="24" fill="none" stroke="var(--ink)" stroke-width="7"/>
        <line x1="56" y1="56" x2="80" y2="80" stroke="var(--ink)" stroke-width="10" stroke-linecap="round"/>
        <text x="38" y="49" text-anchor="middle" font-size="32" font-weight="700" fill="var(--brand-blue)" font-family="Questrial, sans-serif">?</text>
      </svg>
      <span class="pillar-label">Recruit Wisely</span>
    </div>

    <div class="pillar pillar--grow">
      <svg width="90" height="90" viewBox="0 0 90 90" aria-hidden="true">
        <rect x="14" y="76" width="62" height="8" fill="var(--ink)"/>
        <rect x="22" y="40" width="18" height="34" fill="var(--ink)"/>
        <rect x="50" y="30" width="12" height="44" fill="var(--brand-blue)"/>
        <polygon points="56,6 72,30 40,30" fill="var(--brand-blue)"/>
      </svg>
      <span class="pillar-label">Grow Teams</span>
    </div>

    <div class="pillar pillar--reach">
      <svg width="90" height="90" viewBox="0 0 90 90" aria-hidden="true">
        <polyline points="6,80 30,58 46,66 74,36" fill="none" stroke="var(--brand-blue)" stroke-width="8" stroke-linejoin="round"/>
        <polygon points="84,26 80,50 62,34" fill="var(--brand-blue)"/>
      </svg>
      <span class="pillar-label">Reach Goals</span>
    </div>

    <span class="separator separator--one"></span>
    <span class="separator separator--two"></span>

    <div class="partner-badge" role="img" aria-label="Partner badge"></div>
  </section>

  <div class="profile-frame">
    <div class="profile-logo">
      <span class="logo-mark"></span>
      <span class="logo-name">TimberLineMetrics</span>
    </div>
  </div>
</div>
</body>
</html>
```